Colour consulting and Interior design company needs a squarespace web design

we need a website design for squarespace for a Melbourne based company called 'Brightwell Rooms' which incorporates the existing logo. The company primarily provides colour consulting for residential and commercial as well as interior design services. Schemes are personalised for each client. I would like the design to have some colour and use the colour palette provided but it is not is not totally exclusive. The final design should indicate character, playfulness, functionality , harmony and joy. I like the blue/green core colour with the white and would like that to be incorporated.
as per image provided below - double sided
4 page
Requirements
Must have
- space for some images but not too many.
- Page for booking consultation
Should not have
- real images of houses

```html
<!DOCTYPE html>
<html lang="en">
<head>
<meta charset="utf-8">
<title>Brightwell Rooms — Interior Design &amp; Colour Consulting</title>
<link href="https://fonts.googleapis.com/css2?family=Libre+Franklin:wght@300;400;500;600&display=swap" rel="stylesheet">
<style>
  :root {
    --teal: #16748d;
    --teal-deep: #003d48;
    --ink: #1e3a44;
    --panel: #eeeef1;
    --white: #ffffff;
    --border-soft: #b9c0c4;
    --accent-line: #3fb3c4;
  }
  * { box-sizing: border-box; margin: 0; padding: 0; }
  html, body { width: 1200px; height: 2655px; overflow: hidden; background: var(--white); }
  body { position: relative; font-family: "Libre Franklin", Arial, sans-serif; color: var(--ink); }
  .abs { position: absolute; }

  /* header */
  .site-header { left: 0; top: 0; width: 1200px; height: 112px; background: var(--white); }
  .brand { left: 44px; top: 32px; display: flex; align-items: center; gap: 12px; }
  .brand-mark { width: 44px; height: 44px; background: var(--teal); display: block; }
  .brand-name { font-size: 24px; font-weight: 500; color: var(--teal); line-height: 1; white-space: nowrap; }
  .main-nav a { position: absolute; top: 46px; font-size: 14px; color: var(--ink); text-decoration: none; white-space: nowrap; }
  .main-nav a.current { color: var(--teal); }
  .header-phone { left: 761px; top: 46px; font-size: 14px; color: var(--teal); display: flex; align-items: center; gap: 6px; white-space: nowrap; }
  .btn { display: flex; align-items: center; justify-content: center; font-size: 13px; text-decoration: none; white-space: nowrap; }
  .btn-consultant { left: 920px; top: 35px; width: 232px; height: 40px; border: 2px solid var(--accent-line); color: var(--ink); }

  /* hero */
  .hero { left: 0; top: 112px; width: 1200px; height: 534px;
    background: linear-gradient(135deg, #5a534c 0%, #3d3732 40%, #6d655d 70%, #2f2a26 100%); }
  .hero-eyebrow { left: 0; width: 1200px; top: 276px; text-align: center; color: var(--white); font-size: 16px; font-weight: 500; }
  .hero-title { left: 0; width: 1200px; top: 318px; text-align: center; color: var(--white); font-weight: 300; }
  .hero-title span { display: block; white-space: nowrap; }
  .hero-title .l1 { font-size: 46px; line-height: 54px; }
  .hero-title .l2 { font-size: 54px; line-height: 58px; }
  .btn-hero { left: 506px; top: 473px; width: 184px; height: 39px; border: 1.5px solid var(--white); color: var(--white); }

  /* tiles */
  .tile { position: absolute; }
  .panel-light { background: var(--panel); }
  .eyebrow { font-size: 12px; font-weight: 600; color: var(--teal); white-space: nowrap; }
  .lead { font-size: 23px; line-height: 34px; font-weight: 400; white-space: nowrap; }
  .btn-solid { background: var(--teal); color: var(--white); }
  .btn-outline-dark { border: 1.5px solid var(--teal); color: var(--ink); }
  .btn-outline-light { border: 1.5px solid var(--white); color: var(--white); }

  .card-title { position: absolute; left: 0; width: 100%; text-align: center; color: var(--white); }
  .card-title .name { display: block; font-size: 33px; font-weight: 300; }
  .card-title .sub { display: block; font-size: 17px; margin-top: 2px; }

  .handle { position: absolute; bottom: 0; width: 230px; height: 55px; background: var(--white);
    display: flex; align-items: center; gap: 8px; padding-left: 44px; font-size: 13px; color: var(--ink); }
  .handle i { width: 10px; height: 10px; background: var(--teal); display: block; }

  .contact-line { position: absolute; left: 45px; white-space: nowrap; }

  /* footer */
  .site-footer { left: 0; top: 2258px; width: 1200px; height: 397px; background: var(--panel); }
  .footer-brand { left: 0; width: 1200px; top: 2335px; display: flex; justify-content: center; align-items: center; gap: 10px; }
  .footer-brand i { width: 28px; height: 28px; background: var(--teal); display: block; }
  .footer-brand span { font-size: 22px; font-weight: 500; color: var(--teal); }
  .footer-nav { left: 0; width: 1200px; top: 2420px; display: flex; justify-content: center; gap: 22px; font-size: 14px; }
  .social { position: absolute; top: 2478px; width: 38px; height: 38px; border-radius: 50%; border: 1.5px solid var(--border-soft); }
  .social.active { background: var(--teal); border-color: var(--teal); }
  .copyright { left: 0; width: 1200px; top: 2555px; text-align: center; font-size: 13px; line-height: 22px; }
  .copyright small { font-size: 11px; }
</style>
</head>
<body>

<header class="abs site-header">
  <div class="abs brand">
    <span class="brand-mark"></span>
    <span class="brand-name">Brightwell Rooms</span>
  </div>
  <nav class="main-nav">
    <a class="current" style="left:421px">About</a>
    <a style="left:480px">Interior Design</a>
    <a style="left:595px">Projects</a>
    <a style="left:671px">Contact</a>
  </nav>
  <div class="abs header-phone">
    <svg width="12" height="12" viewBox="0 0 24 24"><path fill="#16748d" d="M6.6 10.8a15 15 0 0 0 6.6 6.6l2.2-2.2c.3-.3.7-.4 1-.2 1.1.4 2.3.6 3.6.6.6 0 1 .4 1 1V20c0 .6-.4 1-1 1A17 17 0 0 1 3 4c0-.6.4-1 1-1h3.5c.6 0 1 .4 1 1 0 1.3.2 2.5.6 3.6.1.3 0 .7-.2 1z"/></svg>
    03 - 9412 5530
  </div>
  <a class="abs btn btn-consultant">Request A Colour Consultant</a>
</header>

<section class="abs hero" role="img" aria-label="Loft living room with leather sofa, brick walls and a staircase"></section>
<div class="abs hero-eyebrow">Interior Design / Colour Consulting</div>
<h1 class="abs hero-title"><span class="l1">Your Personality. Your Space.</span><span class="l2">Our Inspiraton.</span></h1>
<a class="abs btn btn-hero">Contact Us Today!</a>

<!-- services row -->
<section class="tile panel-light" style="left:0;top:651px;width:398px;height:397px">
  <div class="abs eyebrow" style="left:44px;top:72px">Colour Consulting Experts</div>
  <p class="abs lead" style="left:44px;top:112px;font-size:22px;line-height:33px">We Specialise in Painting<br>Houses, Apartments,<br>Unit Complexes and Every-<br>thing In-Between</p>
  <a class="abs btn btn-solid" style="left:44px;top:303px;width:138px;height:39px">Consult Now!</a>
</section>
<section class="tile" style="left:403px;top:651px;width:395px;height:397px;background:linear-gradient(160deg,#4f6d8a 0%,#8aa0a8 45%,#4d5e4a 100%)" role="img" aria-label="Modern curved residence with glass walls and a garden">
  <div class="card-title" style="top:163px"><span class="name">Residencial</span><span class="sub">Interior Design</span></div>
</section>
<section class="tile" style="left:804px;top:651px;width:396px;height:397px;background:linear-gradient(200deg,#b7c3cc 0%,#6f7f8d 50%,#3b4754 100%)" role="img" aria-label="Glass office towers seen from below">
  <div class="card-title" style="top:163px"><span class="name">Commercial</span><span class="sub">Interior Design</span></div>
  <svg class="abs" style="left:177px;top:302px" width="40" height="40" viewBox="0 0 40 40"><circle cx="20" cy="20" r="18" fill="none" stroke="#fff" stroke-width="1.5"/><path d="M12 20h15M21 14l6 6-6 6" fill="none" stroke="#fff" stroke-width="1.8"/></svg>
</section>

<!-- about row -->
<section class="tile" style="left:0;top:1053px;width:397px;height:395px;background:linear-gradient(135deg,#3a2e2a 0%,#8b6a5c 50%,#c9b9ac 100%)" role="img" aria-label="Two designers reviewing plans together"></section>
<section class="tile" style="left:403px;top:1053px;width:797px;height:395px;background:var(--teal);color:var(--white)">
  <div class="abs" style="left:43px;top:70px;font-size:12px;font-weight:600">About Brightwell Rooms</div>
  <p class="abs lead" style="left:43px;top:110px;color:var(--white)">Brightwell Rooms is a global design firm with integrated project<br>delivery capabilities. We seamlessly unite strategy, design, project<br>management and delivery to achieve real, measurable results<br>for our clients.</p>
  <a class="abs btn btn-outline-light" style="left:43px;top:303px;width:138px;height:37px">Learn More</a>
</section>

<!-- projects row -->
<section class="tile" style="left:0;top:1455px;width:798px;height:396px;background:linear-gradient(180deg,#b9a79a 0%,#e6e0d8 45%,#d8cfc4 75%,#8a7f76 100%)" role="img" aria-label="Living room with two cream sofas and a brick wall"></section>
<section class="tile panel-light" style="left:805px;top:1455px;width:395px;height:396px">
  <div class="abs eyebrow" style="left:45px;top:72px">Projects</div>
  <p class="abs lead" style="left:45px;top:114px;font-size:22px;line-height:33px">Our environments engage,<br>empower and inspire people<br>to do their best, most satis-<br>fying work.</p>
  <a class="abs btn btn-outline-dark" style="left:45px;top:303px;width:136px;height:37px">View All</a>
</section>

<!-- contact row -->
<section class="tile" style="left:0;top:1857px;width:398px;height:395px;background:linear-gradient(150deg,#e9e6e0 0%,#cfc8be 45%,#6b5a4e 100%)" role="img" aria-label="Bright lounge with fireplace and white sofas">
  <div class="handle" style="left:0"><i></i>@brightwellrooms</div>
</section>
<section class="tile" style="left:403px;top:1857px;width:395px;height:395px;background:var(--teal-deep);color:var(--white)">
  <div class="contact-line" style="top:62px;font-size:13px;font-weight:600">Get in Touch Today!</div>
  <div class="contact-line" style="top:104px;font-size:24px">P. 03 - 9412 5530</div>
  <div class="contact-line" style="top:140px;font-size:13px">e. info@brightwellrooms.com</div>
  <div class="contact-line" style="top:180px;font-size:13px;line-height:23px">Brightwell Rooms<br>48 Carrow Lane, Southbank,<br>VIC 3006</div>
  <a class="abs btn btn-outline-light" style="left:45px;top:293px;width:112px;height:38px">Contact</a>
</section>
<section class="tile" style="left:804px;top:1857px;width:396px;height:395px;background:linear-gradient(135deg,#7a4a32 0%,#a9826a 45%,#4f6a45 100%)" role="img" aria-label="Deck lounge with timber wall and vertical garden">
  <div class="handle" style="left:0"><i></i>@brightwellrooms</div>
</section>

<footer class="abs site-footer"></footer>
<div class="abs footer-brand"><i></i><span>Brightwell Rooms</span></div>
<nav class="abs footer-nav"><span>About</span><span>Interior Design</span><span>Projects</span><span>Contact</span></nav>
<span class="social" style="left:489px"></span>
<span class="social active" style="left:547px"></span>
<span class="social" style="left:604px"></span>
<span class="social" style="left:661px"></span>
<div class="abs copyright">© 2018 Brightwell Rooms.<br><small>All rights reserved.</small></div>

</body>
</html>
```